Simple Easy - Taekwondo brochure

I have the content and an idea of the layout I want. I need it to look nice and sharp.

It's a sided 8.5x11 colored brochure

please feel free to move things around and use the images provided

my website is www.brightpathdojo.example if you need an understanding of what the business is about.

all text content is on the website. please be creative!

Target Market(s)

Mothers...must by family friendly because it's for mothers to bring their kids.

Industry/Entity Type

Martial Art

Font styles to use
Other font styles liked:
• Lato

```html
<!DOCTYPE html>
<html lang="en">
<head>
<meta charset="utf-8">
<title>Bright Path Dojo – Brochure</title>
<link rel="stylesheet" href="https://fonts.googleapis.com/css2?family=Lato:ital,wght@0,400;0,700;0,900;1,700;1,900&display=swap">
<style>
  :root {
    --black: #060606;
    --blue: #1373bf;
    --red: #cf2027;
    --white: #ffffff;
    --map: #e6e4df;
  }
  * { box-sizing: border-box; margin: 0; padding: 0; }
  html, body { width: 1200px; height: 927px; overflow: hidden; background: var(--black); }
  body { font-family: 'Lato', sans-serif; color: var(--white); }
  .brochure { position: relative; width: 1200px; height: 927px; display: flex; }
  .panel { position: relative; width: 400px; height: 927px; overflow: hidden; }

  /* Left panel */
  .panel--bio { background: var(--black); }
  .bio-photo { position: absolute; inset: 0; background: radial-gradient(ellipse at 45% 35%, #2a2a2a 0%, #141414 45%, var(--black) 80%); }
  .bio { position: absolute; left: 25px; top: 14px; width: 345px; }
  .bio h1 { color: var(--blue); font-weight: 900; font-size: 21px; margin-bottom: 16px; }
  .bio p { font-size: 10.2px; line-height: 1.2; font-weight: 700; margin-bottom: 12px; }
  .bio p.bio-current { font-style: italic; }
  .awards-title { position: absolute; left: 0; width: 430px; top: 512px; text-align: center; font-style: italic; font-weight: 900; font-size: 29px; line-height: 1.02; }
  .awards-sub { position: absolute; left: 0; width: 430px; top: 578px; text-align: center; color: var(--red); font-style: italic; font-weight: 700; font-size: 18px; }
  .award { position: absolute; left: 20px; width: 372px; height: 68px; }
  .award svg { position: absolute; inset: 0; }
  .award p { position: absolute; left: 76px; right: 14px; top: 0; height: 68px; display: flex; align-items: center; justify-content: center; text-align: center; font-style: italic; font-weight: 700; font-size: 10.6px; line-height: 1.3; }

  /* Middle panel */
  .panel--offer { background: var(--red); }
  .offer-bg { position: absolute; inset: 0; }
  .quote-mark { position: absolute; left: 0; width: 400px; top: -4px; text-align: center; color: var(--red); font-weight: 900; font-size: 88px; line-height: 1; }
  .quote-name { position: absolute; left: 0; width: 400px; top: 70px; text-align: center; color: var(--black); font-style: italic; font-weight: 900; font-size: 30px; }
  .quote-text { position: absolute; left: 26px; width: 348px; top: 118px; text-align: center; font-size: 11.4px; line-height: 1.28; }
  .offer-title { position: absolute; left: 0; width: 400px; top: 380px; text-align: center; font-weight: 700; font-size: 26px; letter-spacing: .5px; }
  .offer-badge { position: absolute; left: 140px; top: 418px; width: 120px; height: 120px; border-radius: 50%; background: var(--black); border: 3px solid var(--white); display: flex; flex-direction: column; justify-content: center; align-items: center; color: #d8d8d8; font-size: 32px; line-height: 1.15; }
  .offer-text { position: absolute; left: 0; width: 400px; top: 560px; text-align: center; font-style: italic; font-weight: 900; font-size: 21.5px; line-height: 1.28; }
  .cta { position: absolute; left: 0; width: 400px; top: 629px; text-align: center; color: var(--blue); font-weight: 900; font-size: 30px; }
  .phone { position: absolute; left: 0; width: 400px; top: 665px; text-align: center; font-weight: 900; font-size: 30px; }
  .address { position: absolute; left: 0; width: 400px; top: 727px; text-align: center; font-weight: 700; font-size: 9px; line-height: 1.25; }
  .map { position: absolute; left: 64px; top: 760px; width: 270px; height: 150px; background: linear-gradient(135deg, #e9e6de 0%, #dedcd6 50%, #e7e3d6 100%); }

  /* Right panel */
  .panel--cover { background: var(--black); }
  .cover-mark { position: absolute; left: 30px; top: 340px; width: 340px; display: flex; align-items: center; justify-content: center; gap: 12px; color: var(--blue); font-weight: 900; font-size: 30px; }
  .cover-mark span.dot { width: 26px; height: 26px; border-radius: 50%; background: var(--red); display: block; }
  .cover-name { position: absolute; left: 0; width: 400px; top: 598px; text-align: center; color: var(--blue); font-weight: 700; font-size: 30px; }
  .cover-tag { position: absolute; left: 0; width: 400px; top: 642px; text-align: center; color: var(--red); font-size: 26px; }
  .cover-url { position: absolute; left: 0; width: 400px; top: 684px; text-align: center; font-weight: 700; font-size: 21px; }
</style>
</head>
<body>
<main class="brochure">

  <section class="panel panel--bio">
    <div class="bio-photo" role="img" aria-label="Faded photo of the head instructor in uniform"></div>
    <div class="bio">
      <h1>MASTER DAN’S</h1>
      <p>Daniel Reyes, (Master Dan), is the owner and head instructor at Bright Path Dojo. Master Dan is a Central Dojang Council-certified 3rd degree Black Belt. The Central Dojang Council is the overseeing authority of all Black Belts in the world, working with the Global Taekwondo Alliance (GTA); it also oversees taekwondo in the Olympics.</p>
      <p>In 1992, at the age of 8, Master Dan began training under Grand Master Albrecht who achieved the level of 8th Dan in taekwondo under the International Kicking Arts Union (IKU). The IKU is another highly respected global authority for taekwondo.</p>
      <p>When Master Dan entered Middle School and then High School, his years of taekwondo training became invaluable as he participated in wrestling, track, and hockey.</p>
      <p>Master Dan continued his taekwondo training post-high school, and in 2007, began training under Grand Master Oduya who has achieved the level of 6th Dan in Taekwondo, certified by the Council; Grand Master Oduya was also a distinguished member of the National Taekwondo Team that competed around the world.</p>
      <p>While attending Riverside University, Master Dan joined Riverside’s Taekwondo Team. Upon graduating in 2008, he was invited by the University to become the team’s Assistant Coach. Because of his exceptional skill and his ability to positively influence and motivate the team, the University selected him to lead as the coach of the team. Master Dan served as the Head Coach of Riverside University’s Taekwondo Team from 2010-2013.</p>
      <p class="bio-current">In 2013, Master Dan began training under Grand Master Lindqvist, a 9th Dan in Taekwondo, certified by the Council. Master Dan currently trains under Grand Master Lindqvist.</p>
    </div>

    <h2 class="awards-title">AWARDS /<br>ACHIEVEMENTS</h2>
    <p class="awards-sub">(under Master Dan’s leadership)</p>

    <div class="award" style="top:616px">
      <svg viewBox="0 0 372 68"><polygon points="70,7 372,7 340,61 70,61" fill="var(--red)"/><polygon points="19,0 57,0 76,34 57,68 19,68 0,34" fill="var(--blue)"/><circle cx="38" cy="29" r="10" fill="none" stroke="#fff" stroke-width="3"/><path d="M31 37 L27 49 L33 46 L36 50 L38 39 M45 37 L49 49 L43 46 L40 50 L38 39" fill="#fff"/></svg>
      <p>4 National Taekwondo League Championships / GTA sanctioned</p>
    </div>
    <div class="award" style="top:691px">
      <svg viewBox="0 0 372 68"><polygon points="70,7 372,7 340,61 70,61" fill="var(--red)"/><polygon points="19,0 57,0 76,34 57,68 19,68 0,34" fill="var(--blue)"/><circle cx="38" cy="29" r="10" fill="none" stroke="#fff" stroke-width="3"/><path d="M31 37 L27 49 L33 46 L36 50 L38 39 M45 37 L49 49 L43 46 L40 50 L38 39" fill="#fff"/></svg>
      <p>10 State Medalists National Taekwondo League State Championships / GTA sanctioned</p>
    </div>
    <div class="award" style="top:766px">
      <svg viewBox="0 0 372 68"><polygon points="70,7 372,7 340,61 70,61" fill="var(--red)"/><polygon points="19,0 57,0 76,34 57,68 19,68 0,34" fill="var(--blue)"/><circle cx="38" cy="29" r="10" fill="none" stroke="#fff" stroke-width="3"/><path d="M31 37 L27 49 L33 46 L36 50 L38 39 M45 37 L49 49 L43 46 L40 50 L38 39" fill="#fff"/></svg>
      <p>12 Atlantic Collegiate Taekwondo Circuit (ACTC) Team Medals / GTA sanctioned</p>
    </div>
    <div class="award" style="top:842px">
      <svg viewBox="0 0 372 68"><polygon points="70,7 372,7 340,61 70,61" fill="var(--red)"/><polygon points="19,0 57,0 76,34 57,68 19,68 0,34" fill="var(--blue)"/><circle cx="38" cy="29" r="10" fill="none" stroke="#fff" stroke-width="3"/><path d="M31 37 L27 49 L33 46 L36 50 L38 39 M45 37 L49 49 L43 46 L40 50 L38 39" fill="#fff"/></svg>
      <p>1 Atlantic Collegiate Taekwondo Circuit (ACTC) TOP DIVISION TEAM TITLES / GTA sanctioned</p>
    </div>
  </section>

  <section class="panel panel--offer">
    <svg class="offer-bg" viewBox="0 0 400 927" preserveAspectRatio="none">
      <polygon points="0,0 400,0 400,252 0,392" fill="var(--black)"/>
      <polygon points="0,0 400,0 400,258 0,384" fill="var(--blue)"/>
    </svg>
    <div class="quote-mark">”</div>
    <h2 class="quote-name">Nora K.</h2>
    <p class="quote-text">I started taking classes with Master Dan a little over 3 years ago. As the newest member of the class, I was shy and unsure of myself. However, I quickly overcame those feelings because Master Dan is a natural teacher. Paired with his passion for the sport, his gift for teaching makes him one of the best coaches I have encountered. I have seen him work with both children and adults and his manner is unfailingly supportive and encouraging. As a teacher myself, I see how he tailors his teaching style to each student and I hope to follow his example in my classroom. I am thankful that my first experience with taekwondo has been through Master Dan’s class.</p>

    <h2 class="offer-title">SPECIAL OFFER</h2>
    <div class="offer-badge"><span>50%</span><span>off</span></div>
    <p class="offer-text">TRIAL LESSON AND GET<br>FREE T-SHIRT</p>
    <p class="cta">CALL US TODAY!</p>
    <p class="phone">555-014-2768</p>
    <p class="address">2870, Millbrook Road<br>Oak Hollow, PA 19000</p>
    <div class="map" role="img" aria-label="Street map showing the dojo location"></div>
  </section>

  <section class="panel panel--cover">
    <div class="cover-mark"><span class="dot"></span><span>Bright Path Dojo</span></div>
    <h2 class="cover-name">Bright Path Dojo</h2>
    <p class="cover-tag">Focus Your Child’s Potential</p>
    <p class="cover-url">www.brightpathdojo.example</p>
  </section>

</main>
</body>
</html>
```